Nightclub promoter business cards

We need business cards designed for our company based in Toronto, Canada called "NowQuillo". We are an events company that promotes weekly parties in the city. We cater to a 25+ crowd and feel like our brand should reflect that. We are looking for business cards that are textured and contain a unique design. We would prefer black cards. The final design should communicate the finest hospitality and prestige. I've attached files containing our logo. For more info. about our brand visit our website at www.nowquillo-example.com.

Industry/Entity Type

Business

```html
<!DOCTYPE html>
<html lang="en">
<head>
<meta charset="utf-8">
<title>NowQuillo — Business Cards</title>
<link rel="stylesheet" href="https://fonts.googleapis.com/css2?family=Oswald:wght@400&family=Great+Vibes&family=Tinos:ital,wght@0,400;0,700;1,400&display=swap">
<style>
  :root {
    --page: #e4e1dc;
    --card-black: #161314;
    --card-black-soft: #231f20;
    --dot-tone: #3a3532;
    --ornament-light: #c9cdc8;
    --ornament-mid: #8c918b;
    --panel-white: #ffffff;
    --panel-edge: #6f726d;
    --ink: #111111;
    --sage: #b7c2b5;
    --band-grey: #7d807b;
    --band-line: #a6aaa4;
  }
  * { box-sizing: border-box; margin: 0; padding: 0; }
  html, body {
    width: 1200px;
    height: 843px;
    overflow: hidden;
    background: var(--page);
  }
  .canvas {
    position: relative;
    width: 1200px;
    height: 843px;
  }
  .card {
    position: absolute;
    top: 267px;
    width: 540px;
    height: 309px;
    border-radius: 6px;
    overflow: hidden;
    box-shadow: 0 8px 22px rgba(0,0,0,0.28);
  }

  /* ---------- Contact side ---------- */
  .card--contact {
    left: 40px;
    background: var(--card-black);
  }
  .card--contact .dot-field {
    position: absolute;
    inset: 0;
    background: linear-gradient(135deg, var(--card-black-soft), var(--card-black) 60%);
  }
  .card--contact .ornament-frame {
    position: absolute;
    left: 95px;
    top: 22px;
    width: 350px;
    height: 250px;
    border-radius: 40%;
    background: radial-gradient(ellipse at center, var(--ornament-light) 0%, var(--ornament-mid) 55%, rgba(140,145,139,0) 72%);
  }
  .contact-panel {
    position: absolute;
    left: 165px;
    top: 52px;
    width: 215px;
    height: 170px;
    background: var(--panel-white);
    border: 4px solid var(--panel-edge);
    border-radius: 22px;
    padding: 26px 18px 0 20px;
    font-family: "Tinos", "Times New Roman", serif;
    color: var(--ink);
  }
  .contact-panel .phone {
    font-weight: 700;
    font-size: 15px;
    letter-spacing: 0.5px;
    margin-bottom: 12px;
  }
  .contact-panel .line {
    font-size: 14px;
    line-height: 22px;
    white-space: nowrap;
  }
  .tagline {
    position: absolute;
    left: 0;
    right: 0;
    top: 238px;
    text-align: center;
    font-family: "Tinos", "Times New Roman", serif;
    font-style: italic;
    font-size: 12px;
    color: var(--ornament-light);
  }

  /* ---------- Brand side ---------- */
  .card--brand {
    left: 620px;
    background: linear-gradient(160deg, #2a2627 0%, var(--card-black) 45%, #0f0d0e 100%);
  }
  .card--brand .ornament-cluster {
    position: absolute;
    left: 30px;
    top: 30px;
    width: 210px;
    height: 250px;
    border-radius: 45%;
    background: radial-gradient(ellipse at 55% 50%, var(--ornament-light) 0%, var(--ornament-mid) 45%, rgba(140,145,139,0) 72%);
  }
  .card--brand .stripe-band {
    position: absolute;
    left: 228px;
    top: 0;
    width: 40px;
    height: 100%;
    background: var(--band-grey);
    border-left: 3px solid var(--band-line);
    border-right: 3px solid var(--band-line);
  }
  .brand-name {
    position: absolute;
    left: 300px;
    top: 108px;
    font-family: "Oswald", "Arial Narrow", sans-serif;
    font-weight: 400;
    font-size: 50px;
    line-height: 1;
    color: var(--sage);
    letter-spacing: 0.5px;
  }
  .brand-sub {
    position: absolute;
    left: 318px;
    top: 168px;
    font-family: "Great Vibes", cursive;
    font-size: 20px;
    color: var(--sage);
  }
</style>
</head>
<body>
<main class="canvas">

  <section class="card card--contact" aria-label="Contact side of the business card">
    <div class="dot-field" role="img" aria-label="Black card with a soft grey polka-dot pattern"></div>
    <div class="ornament-frame" role="img" aria-label="Silver-grey floral scroll ornament framing the contact panel"></div>
    <div class="contact-panel">
      <p class="phone">+1 647 555 0148</p>
      <p class="line">vip@nowquillo-example.com</p>
      <p class="line">www.nowquillo-example.com</p>
    </div>
    <p class="tagline">If it's NowQuillo you'll know</p>
  </section>

  <section class="card card--brand" aria-label="Brand side of the business card">
    <div class="ornament-cluster" role="img" aria-label="Large silver-grey floral flourish ornament"></div>
    <div class="stripe-band"></div>
    <p class="brand-name">NowQuillo</p>
    <p class="brand-sub">Events and Catering</p>
  </section>

</main>
</body>
</html>
```